Organic rose water based skincare line in need of product label and packaging design

We are looking for a simple, clean, modern labeling and packaging design for 2 of our products. Our brand's demographic is upscale females ages 20-40. We want our packaging to be very minimalistic, and instagramable.

Product #1: Rose water facial spray "Lumi Mist"
Product #2: Rose water facial toner "Velvet Hush Hour"

Please see attached images for our current logo and label design. We have also added some images that inspire our branding.

Target Market(s)

trendy woman ages 20-40

Industry/Entity Type

Skin Care Product

Font styles to use
Serif
Sans Serif

Colors

Designer to choose only greyscale colors for use in the design.

Requirements
Must have
• Must have our logo, bottle size, product name on front and how to use and ingredient on the back. Please see project description and attached images for more information.
Should not have
• Too much going on or too many colors.

```html
<!DOCTYPE html>
<html lang="en">
<head>
<meta charset="utf-8">
<title>Lumi Mist — Label</title>
<link href="https://fonts.googleapis.com/css2?family=Raleway:wght@200;400;600&display=swap" rel="stylesheet">
<style>
  :root {
    --paper: #ffffff;
    --ink: #000000;
    --divider: #8a8a8a;
    --dot: #7a7a7a;
    --bloom: #ececec;
    --bloom-edge: #dcdcdc;
  }
  * { margin: 0; padding: 0; box-sizing: border-box; }
  html, body { width: 1200px; height: 1180px; overflow: hidden; background: var(--paper); }
  .label {
    position: relative;
    width: 1200px;
    height: 1180px;
    background: var(--paper);
    font-family: "Raleway", sans-serif;
    color: var(--ink);
    overflow: hidden;
  }
  .decor { position: absolute; inset: 0; }
  .divider {
    position: absolute;
    left: 600px; top: 75px;
    width: 1px; height: 1030px;
    background: var(--divider);
  }
  .centered { position: absolute; transform: translateX(-50%); text-align: center; white-space: nowrap; }

  .brand-name {
    left: 292px; top: 148px;
    font-weight: 600;
    font-size: 44px;
    line-height: 46px;
    text-align: left;
    letter-spacing: -0.5px;
  }
  .product-name {
    left: 300px; top: 335px;
    font-weight: 200;
    font-size: 96px;
    line-height: 1;
    letter-spacing: 1px;
  }
  .product-sub {
    left: 285px; top: 444px;
    font-size: 20px;
    line-height: 33px;
  }
  .volume {
    left: 287px; top: 900px;
    font-size: 20px;
  }

  .section-title {
    font-weight: 600;
    font-size: 20px;
    letter-spacing: 0.2px;
  }
  .use-title { left: 913px; top: 583px; }
  .use-text { left: 913px; top: 632px; font-size: 20px; line-height: 26px; }
  .benefits-title { left: 913px; top: 803px; }
  .benefits-list {
    left: 913px; top: 856px;
    list-style: none;
    font-size: 20px;
    line-height: 32.8px;
  }
</style>
</head>
<body>
<main class="label">
  <svg class="decor" width="1200" height="1180" viewBox="0 0 1200 1180" aria-hidden="false">
    <g role="img" aria-label="Line-drawn rose blossoms scattered as decoration">
      <g fill="var(--bloom)" stroke="var(--bloom-edge)" stroke-width="1.5">
        <circle cx="25" cy="19" r="43"/>
        <circle cx="676" cy="12" r="75"/>
        <circle cx="1138" cy="99" r="40"/>
        <circle cx="893" cy="313" r="88"/>
        <circle cx="108" cy="1141" r="115"/>
        <circle cx="366" cy="1042" r="68"/>
        <circle cx="503" cy="1153" r="40"/>
        <circle cx="874" cy="1153" r="90"/>
        <circle cx="1190" cy="1045" r="38"/>
      </g>
    </g>
    <g class="dots" fill="var(--dot)">
      <circle cx="319" cy="650" r="3.5"/>
      <circle cx="526" cy="646" r="2.5"/>
      <circle cx="139" cy="667" r="2.5"/>
      <circle cx="455" cy="720" r="2.5"/>
      <circle cx="182" cy="770" r="2.5"/>
      <circle cx="552" cy="867" r="4"/>
      <circle cx="99" cy="884" r="4"/>
      <circle cx="254" cy="936" r="2.5"/>
      <circle cx="171" cy="985" r="3.5"/>
      <circle cx="428" cy="962" r="5"/>
      <circle cx="458" cy="1074" r="5"/>
      <circle cx="296" cy="1114" r="5"/>
      <circle cx="704" cy="171" r="2.5"/>
      <circle cx="1094" cy="156" r="2.5"/>
      <circle cx="695" cy="404" r="2.5"/>
      <circle cx="882" cy="468" r="3.5"/>
      <circle cx="1017" cy="539" r="2.5"/>
      <circle cx="662" cy="703" r="3.5"/>
      <circle cx="1115" cy="686" r="3.5"/>
      <circle cx="817" cy="755" r="2.5"/>
      <circle cx="734" cy="803" r="3.5"/>
      <circle cx="689" cy="1083" r="5"/>
      <circle cx="1085" cy="1076" r="5"/>
    </g>
  </svg>

  <div class="divider"></div>

  <section class="front">
    <div class="brand-name centered">the<br>petal<br>studio</div>
    <h1 class="product-name centered">LUMI MIST</h1>
    <p class="product-sub centered">Organic rosewater<br>Hydrating mist</p>
    <p class="volume centered">2 oz/60ml</p>
  </section>

  <section class="back">
    <h2 class="section-title use-title centered">TO USE</h2>
    <p class="use-text centered">Mist over<br>face + body + hair<br>as desired for hydration</p>
    <h2 class="section-title benefits-title centered">ORGANIC ROSE WATER</h2>
    <ul class="benefits-list centered">
      <li>Hydrates</li>
      <li>fights acne</li>
      <li>mantains skin’s pH</li>
      <li>strengthens skin cells</li>
      <li>prevents fine lines &amp; wrinkles</li>
    </ul>
  </section>
</main>
</body>
</html>
```